Designs for a Barrister's chambers

Design stationery (including business card and letterhead) for a barrister's chambers -- similar to a law firm, using the enclosed logo. The current designs are not fit for purpose.

```html
<!DOCTYPE html>
<html lang="en">
<head>
<meta charset="utf-8">
<title>Ashgrove Chambers – Business Card</title>
<link href="https://fonts.googleapis.com/css2?family=Outfit:wght@600&family=Open+Sans:wght@600;700&family=Roboto:wght@500&display=swap" rel="stylesheet">
<style>
  :root {
    --backdrop: #9ccae8;
    --navy: #141f33;
    --navy-mid: #1f2d47;
    --navy-soft: #2e3f5a;
    --teal: #1b95b4;
    --white: #ffffff;
    --ink: #141f33;
  }
  * { margin: 0; padding: 0; box-sizing: border-box; }
  html, body { width: 1200px; height: 1200px; overflow: hidden; }
  body { background: var(--backdrop); position: relative; }

  .card { position: absolute; overflow: hidden; box-shadow: 0 6px 18px rgba(20, 31, 51, 0.35); }

  /* Front */
  .card-front { left: 261px; top: 111px; width: 677px; height: 398px; background: var(--navy); }
  .front-rule { position: absolute; top: 194px; height: 4px; background: var(--white); }
  .front-rule.left { left: 0; width: 166px; }
  .front-rule.right { left: 503px; right: 0; }
  .front-mark { position: absolute; left: 181px; top: 158px; width: 78px; height: 78px; background: var(--teal); }
  .front-name {
    position: absolute; left: 276px; top: 152px;
    font-family: "Outfit", sans-serif; font-weight: 600; font-size: 45px; line-height: 45px;
    color: var(--white); letter-spacing: -0.5px;
  }

  /* Back */
  .card-back { left: 262px; top: 641px; width: 675px; height: 386px; background: var(--white); }
  .back-graphics { position: absolute; inset: 0; }
  .person-name {
    position: absolute; left: 43px; top: 46px;
    font-family: "Open Sans", sans-serif; font-weight: 700; font-size: 25px; letter-spacing: 1.6px;
    color: var(--ink); word-spacing: 6px;
  }
  .person-role {
    position: absolute; left: 44px; top: 78px;
    font-family: "Open Sans", sans-serif; font-weight: 700; font-size: 18px; color: var(--teal);
  }
  .name-rule { position: absolute; left: 42px; top: 106px; width: 300px; height: 2px; background: var(--teal); }

  .back-mark { position: absolute; left: 446px; top: 48px; width: 48px; height: 48px; background: var(--teal); }
  .back-name {
    position: absolute; left: 503px; top: 44px;
    font-family: "Outfit", sans-serif; font-weight: 600; font-size: 27px; line-height: 29px;
    color: var(--ink); letter-spacing: -0.3px;
  }

  .contact-rail { position: absolute; left: 43px; top: 146px; width: 26px; height: 137px; border-radius: 13px; background: var(--navy); }
  .contact-icon { position: absolute; left: 5px; width: 16px; height: 16px; fill: var(--white); }
  .contact-list { position: absolute; left: 84px; top: 146px; list-style: none; }
  .contact-list li {
    position: absolute; left: 0; white-space: nowrap;
    font-family: "Roboto", sans-serif; font-weight: 500; font-size: 14px; color: var(--ink);
  }
</style>
</head>
<body>

<section class="card card-front">
  <div class="front-rule left"></div>
  <div class="front-rule right"></div>
  <div class="front-mark"></div>
  <div class="front-name">Ashgrove<br>Chambers</div>
</section>

<section class="card card-back">
  <svg class="back-graphics" viewBox="0 0 675 386" width="675" height="386" aria-hidden="true">
    <polygon points="0,338 271,338 225,386 0,386" fill="#2e3f5a"/>
    <polygon points="271,338 390,338 343,386 225,386" fill="#1f2d47"/>
    <polygon points="390,338 675,338 675,386 343,386" fill="#141f33"/>
    <polygon points="495,386 675,206 675,241 530,386" fill="#ffffff"/>
    <polygon points="425,386 675,136 675,206 495,386" fill="#1b95b4"/>
    <polygon points="530,386 675,241 675,386" fill="#141f33"/>
  </svg>

  <div class="person-name">MARCUS HALLWORTH</div>
  <div class="person-role">Barrister</div>
  <div class="name-rule"></div>

  <div class="back-mark"></div>
  <div class="back-name">Ashgrove<br>Chambers</div>

  <div class="contact-rail">
    <svg class="contact-icon" style="top:12px" viewBox="0 0 16 16"><path d="M8 0.5a5.5 5.5 0 0 0-5.5 5.5c0 4 5.5 9.5 5.5 9.5s5.5-5.5 5.5-9.5A5.5 5.5 0 0 0 8 0.5zm0 8a2.5 2.5 0 1 1 0-5 2.5 2.5 0 0 1 0 5z"/></svg>
    <svg class="contact-icon" style="top:45px" viewBox="0 0 16 16"><path d="M3.6 1l2.4 3-1.4 1.6c.9 2 2.6 3.8 4.7 4.8l1.6-1.4 3 2.4-1.6 2.4C6.8 13.6 2.4 9.2 1.2 3.8z"/></svg>
    <svg class="contact-icon" style="top:77px" viewBox="0 0 16 16"><path d="M0.5 3h15v10h-15zM1.8 4.2v.3L8 9l6.2-4.5v-.3zM1.8 6v5.8l4-2.9zm12.4 0l-4 2.9 4 2.9zM6.8 9.6l-4.9 2.2h12.2L9.2 9.6 8 10.5z" fill-rule="evenodd"/></svg>
    <svg class="contact-icon" style="top:107px" viewBox="0 0 16 16"><path d="M4 1v12.5l3-3 2.2 4.8 2-1-2.2-4.6h4.2z"/></svg>
  </div>

  <ul class="contact-list">
    <li style="top:12px">48 Quill Lane, London, EC2B 7MR</li>
    <li style="top:45px">+020 7946 0101 /+020 7946 0102</li>
    <li style="top:76px">marcus.hallworth@ashgrovechambers.com</li>
    <li style="top:106px">www.ashgrovechambers.com</li>
  </ul>
</section>

</body>
</html>
```